Brochure Design Project for Home Watch company

We are a new start up company in fast growing home watch industry. We provide services in Hawaii so the design needs to be reflect that. Our web site can give you overview of what we do - www.breezekeepcare.com. We will service clients that own second homes in Hawaii. These properties are not necessarily income producing properties for our clients. I'm looking for 2 or 4 page brochure which will be used to market our services to potential new clients. It needs to be high quality, modern with slight Hawaiian feel (we are based on Oahu). I'm not looking for a trifold type of brochure.

We are open to various colors based on what the designer might suggest but as you can see on our home page - the main picture of the home on our site has lots of red and white which we like as well as the "head" or dot above the "i" in our logo is red. I was not able to upload the file of the main house (purchased on snapmeadow) on here therefore I'll have to provide the original photo to the selected designer at the later time. For now I just uploaded the not purchased copy.

If you have other questions please do let me know. And lastly, I will be looking to create a business card and post card as well.

```html
<!DOCTYPE html>
<html lang="en">
<head>
<meta charset="utf-8">
<title>Breeze Keep Care – Flyer</title>
<link rel="stylesheet" href="https://fonts.googleapis.com/css2?family=Roboto:wght@300;400;500;700&family=Roboto+Condensed:wght@400;500&display=swap">
<style>
  :root{
    --coral:#f25454;
    --coral-dark:#e03c3c;
    --ink:#111;
    --body:#222;
    --white:#fff;
    --stage:#e9e9e9;
    --photo-top:#3d4a5c;
    --photo-bottom:#1f3340;
  }
  *{box-sizing:border-box;margin:0;padding:0}
  html,body{width:1200px;height:1200px;overflow:hidden;background:var(--stage)}
  body{font-family:"Roboto",sans-serif;color:var(--body);position:relative}
  .flyer{position:absolute;left:197px;top:31px;width:806px;height:1138px;background:var(--white);overflow:hidden}
  .hero-art{position:absolute;left:0;top:0}
  .device-art{position:absolute;left:470px;top:120px;width:336px;height:490px;border-radius:18px;
    background:linear-gradient(160deg,#2a2a2a 0%,#6d7680 40%,#e8e6df 70%,#d9d7d0 100%)}
  .badge{position:absolute;left:530px;top:26px;width:250px;height:74px;background:var(--white)}
  .brand{position:absolute;left:0;width:474px;text-align:center;color:var(--white);font-weight:400;font-size:64px;line-height:68px}
  .brand--one{top:183px}
  .brand--two{top:252px}
  .brand-dot{display:inline-block;width:14px;height:14px;border-radius:50%;background:var(--coral);margin-left:6px;vertical-align:top;margin-top:8px}
  .tagline{position:absolute;left:27px;top:334px;color:var(--white);font-weight:700;font-size:16px}
  .services-title{position:absolute;left:25px;top:524px;color:var(--coral);font-weight:500;font-size:34px}
  .services-sub{position:absolute;left:25px;top:565px;color:var(--ink);font-weight:300;font-size:32px}
  .tabs{position:absolute;left:27px;top:628px;width:752px;height:48px;background:var(--coral);border-radius:10px;display:flex;align-items:center}
  .tab{font-family:"Roboto Condensed",sans-serif;font-weight:500;font-size:25px;color:var(--white);text-align:center;position:relative}
  .tab--outdoor{width:264px}
  .tab--exterior{width:235px;border-left:3px solid var(--white);border-right:3px solid var(--white);height:34px;line-height:34px}
  .tab--interior{flex:1}
  .col{position:absolute;font-weight:500;font-size:16px;line-height:20.3px;color:var(--ink)}
  .col--outdoor{left:52px;top:696px;width:200px}
  .col--exterior{left:305px;top:698px;width:200px}
  .col--interior{left:552px;top:695px;width:210px}
  .start-banner{position:absolute;left:0;top:903px}
  .start-text{position:absolute;left:26px;top:906px;color:var(--white);font-weight:500;font-size:26px}
  .member-title{position:absolute;left:26px;top:954px;color:var(--coral);font-weight:500;font-size:27px}
  .member-copy{position:absolute;left:27px;top:988px;width:320px;font-weight:300;font-size:17.5px;line-height:21.8px;color:var(--ink)}
  .steps-copy{position:absolute;left:393px;top:919px;width:385px;font-weight:300;font-size:17.5px;line-height:21.6px;color:var(--ink)}
  .steps-copy b{font-weight:700}
  .footer{position:absolute;left:0;top:1087px;width:806px;height:51px;background:var(--coral);display:flex;justify-content:center;align-items:center;gap:12px;color:var(--white);font-size:19px}
  .footer .sep{opacity:.9}
  .footer svg{width:13px;height:13px;vertical-align:-1px;margin-right:4px}
</style>
</head>
<body>
<main class="flyer">
  <svg class="hero-art" width="806" height="540" viewBox="0 0 806 540">
    <defs>
      <linearGradient id="heroTone" x1="0" y1="0" x2="0" y2="1">
        <stop offset="0" stop-color="var(--photo-top)"/>
        <stop offset="0.55" stop-color="#4a4038"/>
        <stop offset="1" stop-color="var(--photo-bottom)"/>
      </linearGradient>
    </defs>
    <rect role="img" aria-label="Photo of a tropical villa with pool and palm trees at dusk" width="806" height="520" fill="url(#heroTone)"/>
    <path d="M0 425 C120 470 300 500 520 500 L806 500 L806 540 L0 540 Z" fill="var(--coral)"/>
    <path d="M0 470 C150 500 320 512 500 512 L806 512 L806 540 L0 540 Z" fill="var(--white)"/>
  </svg>

  <div class="device-art" role="img" aria-label="Laptop and tablet showing a home watch report checklist over a house photo"></div>
  <div class="badge" role="img" aria-label="Accredited member badge"></div>

  <div class="brand brand--one">Breeze<span class="brand-dot"></span></div>
  <div class="brand brand--two">Keep Care</div>
  <div class="tagline">Providing Premiere Home Watch and Concierge Services</div>

  <h2 class="services-title">SERVICES</h2>
  <p class="services-sub">Primary Home Watch includes:</p>

  <div class="tabs">
    <div class="tab tab--outdoor">General Outdoor</div>
    <div class="tab tab--exterior">Home Exterior</div>
    <div class="tab tab--interior">Home Interior</div>
  </div>

  <p class="col col--outdoor">Check yard, lawn and landscaping; check lanai, deck, and pool area for any damage; check for mold or fading of all outdoor furniture; check water level of swimming pool or hot tub, if applicable</p>
  <p class="col col--exterior">Check security cameras; check for overall damage; remove mail, newspapers, and flyers from mailbox and store inside of the property; check outdoor plumbing and hoses for leakage; check garage; check for vandalism and theft</p>
  <p class="col col--interior">Make sure security system is in working order; ensure that all doors, windows and sliders are locked and secured; check thermostats and make sure the air conditioning is set at appropriate and requested temperature; make sure all smoke detectors</p>

  <svg class="start-banner" width="380" height="48" viewBox="0 0 380 48">
    <path d="M0 0 H326 L346 22 L326 44 H0 Z" fill="var(--coral)"/>
    <path d="M333 0 L353 22 L333 44" fill="none" stroke="var(--coral)" stroke-width="5"/>
    <path d="M344 0 L364 22 L344 44" fill="none" stroke="var(--coral)" stroke-width="5"/>
    <path d="M355 0 L375 22 L355 44" fill="none" stroke="var(--coral)" stroke-width="5"/>
  </svg>
  <div class="start-text">How do you get started?</div>

  <h3 class="member-title">Member of HWGA</h3>
  <p class="member-copy">We are Accredited Members of the HWGA. We are insured and bonded, and we agreed to uphold the strictest and most ethical standards in the industry</p>

  <p class="steps-copy">First <b>contact us.</b> Then we’ll send you an <b>application</b> to fill out. Within 24 hours we’ll send you a <b>quote</b> and follow up via phone call to discuss details and answer any questions you might have, and then, finally, we’ll send you our <b>service agreement</b> via email for your electronic signature</p>

  <footer class="footer">
    <span><svg viewBox="0 0 16 16"><path d="M3 1 L6 1 L7 5 L5 6.5 C6 9 7 10 9.5 11 L11 9 L15 10 L15 13 C15 14 14 15 13 15 C6 15 1 10 1 3 C1 2 2 1 3 1 Z" fill="#fff"/></svg>808-555-0142</span>
    <span class="sep">|</span>
    <span><svg viewBox="0 0 16 16"><path d="M6 10 L10 6 M7 4 L9 2 A3 3 0 0 1 14 7 L12 9 M9 12 L7 14 A3 3 0 0 1 2 9 L4 7" fill="none" stroke="#fff" stroke-width="2"/></svg>www.breezekeepcare.com</span>
    <span class="sep">|</span>
    <span><svg viewBox="0 0 16 16"><rect x="1" y="3" width="14" height="10" fill="none" stroke="#fff" stroke-width="1.8"/><path d="M1 3 L8 9 L15 3" fill="none" stroke="#fff" stroke-width="1.8"/></svg>hello@breezekeepcare.com</span>
  </footer>
</main>
</body>
</html>
```